Marta Belcourt Name Card Design

Hello Designers,
I wanna have a name card with these details below:
Name: Marta Belcourt
Job Title: Doctor
Address: 2318 Ferris Lane, Tacoma, WA, US
Phone: 8273360915
Slogan on card: Health care 24/7, Whenever you need, we're there!
I love yellows colors, red and white. It would be nice if my card would be designed with these colors.

```html
<!DOCTYPE html>
<html lang="en">
<head>
<meta charset="utf-8">
<title>Marta Belcourt Name Card</title>
<link href="https://fonts.googleapis.com/css2?family=Exo+2:wght@400;600;700&family=Roboto+Condensed:wght@400&display=swap" rel="stylesheet">
<style>
  :root {
    --stage: #e7e4df;
    --card-orange: #f0a000;
    --glow: #ffd889;
    --emblem-tone: #d9902a;
    --slot-shadow: rgba(120, 60, 0, 0.35);
    --paper: #ffffff;
    --ink-grey: #5a5a5a;
    --ink-soft: #8a8a8a;
    --accent-red: #d8541f;
    --white: #ffffff;
  }
  html, body {
    margin: 0;
    width: 1200px;
    height: 872px;
    overflow: hidden;
    background: var(--stage);
  }
  .canvas {
    position: relative;
    width: 1200px;
    height: 872px;
  }
  .card {
    position: absolute;
    left: 280px;
    width: 640px;
    height: 366px;
    background: var(--card-orange);
    border-radius: 4px;
    overflow: hidden;
    box-shadow: 0 10px 24px rgba(0,0,0,0.18);
    font-family: "Exo 2", sans-serif;
  }
  .card--contact { top: 46px; }
  .card--name { top: 460px; }

  .emblem-area {
    position: absolute;
    left: 20px;
    top: 40px;
    width: 230px;
    height: 230px;
    border-radius: 50%;
    background: radial-gradient(circle, rgba(217,144,42,0.55) 0%, var(--glow) 28%, rgba(255,216,137,0.45) 45%, rgba(240,160,0,0) 70%);
  }
  .slot {
    position: absolute;
    left: 222px;
    top: 70px;
    width: 4px;
    height: 226px;
    border-radius: 2px;
    background: var(--slot-shadow);
    box-shadow: -4px 0 10px rgba(255,230,170,0.6);
  }

  .strip {
    position: absolute;
    left: 224px;
    height: 36px;
    background: var(--paper);
    box-shadow: 2px 4px 6px rgba(0,0,0,0.25);
    font-family: "Roboto Condensed", sans-serif;
    color: var(--ink-grey);
    font-size: 20px;
    line-height: 36px;
    padding-left: 18px;
    white-space: nowrap;
    transform-origin: left center;
    box-sizing: border-box;
  }
  .strip--email { top: 110px; width: 270px; transform: rotate(-3deg); }
  .strip--address { top: 164px; width: 300px; transform: rotate(1deg); }
  .strip--phone { top: 218px; width: 190px; transform: rotate(4deg); font-size: 24px; }

  .slogan {
    position: absolute;
    left: 34px;
    bottom: 26px;
    margin: 0;
    color: var(--white);
    font-size: 17px;
    font-weight: 400;
    letter-spacing: 0.3px;
    display: flex;
    align-items: center;
    gap: 10px;
  }
  .slogan__dot {
    width: 18px;
    height: 18px;
    border-radius: 50%;
    background: var(--accent-red);
  }

  .name-tab {
    position: absolute;
    left: 224px;
    top: 92px;
    width: 340px;
    height: 176px;
    background: var(--paper);
    border-radius: 0 24px 24px 0;
    box-shadow: 3px 5px 10px rgba(0,0,0,0.25);
    box-sizing: border-box;
    padding: 22px 26px 0 30px;
  }
  .name-tab__name {
    margin: 0;
    color: var(--ink-grey);
    font-size: 44px;
    font-weight: 700;
    line-height: 1.02;
  }
  .name-tab__title {
    margin: 6px 0 0;
    text-align: right;
    color: var(--ink-soft);
    font-size: 15px;
    font-weight: 400;
  }
</style>
</head>
<body>
<main class="canvas">

  <section class="card card--contact" aria-label="Card back with contact details">
    <div class="emblem-area" role="img" aria-label="Emblem area for the 24 hour service mark"></div>
    <div class="slot"></div>
    <div class="strip strip--email">care@belcourtmd.com</div>
    <div class="strip strip--address">2318 Ferris Lane, Tacoma, WA, US</div>
    <div class="strip strip--phone">8273360915</div>
    <p class="slogan">Health care 24/7 , Whenever you need, we're there!</p>
  </section>

  <section class="card card--name" aria-label="Card front with name">
    <div class="emblem-area" role="img" aria-label="Emblem area for the practice mark"></div>
    <div class="slot"></div>
    <div class="name-tab">
      <h1 class="name-tab__name">Marta<br>Belcourt</h1>
      <p class="name-tab__title">Doctor</p>
    </div>
    <p class="slogan"><span class="slogan__dot"></span>Health care 24/7 , Whenever you need, we're there!</p>
  </section>

</main>
</body>
</html>
```